Yard Sign Design Needed

Yard sign needed for mowing & landscaping company. Would like to use the top logo with black background which is attached. Would like MOWING to be in large standout letters. The word "landscaping" can be smaller and more artistic or omitted. Will need room for phone number once design is approved. The phone number will need to stand out and look identical/similar to the word 'MOWING"

```html
<!DOCTYPE html>
<html lang="en">
<head>
<meta charset="utf-8">
<title>Brantley Grounds LLC – Mowing Yard Sign</title>
<link rel="stylesheet" href="https://fonts.googleapis.com/css2?family=Orbitron:wght@700;900&family=Exo+2:wght@600;700&display=swap">
<style>
  :root {
    --page-bg: #e8eae5;
    --sign-black: #050505;
    --sign-lime: #a9ba1d;
    --brand-lime: #94b81c;
    --ink-black: #000000;
    --ink-white: #ffffff;
  }
  html, body {
    margin: 0;
    padding: 0;
    width: 1200px;
    height: 970px;
    overflow: hidden;
    background: var(--page-bg);
  }
  .yard-sign {
    position: absolute;
    left: 161px;
    top: 35px;
    width: 878px;
    height: 900px;
    display: flex;
    flex-direction: column;
  }
  .brand-panel {
    position: relative;
    height: 444px;
    background: var(--sign-black);
  }
  .brand-mark {
    position: absolute;
    left: 70px;
    top: 140px;
    width: 150px;
    height: 150px;
    background: var(--brand-lime);
  }
  .brand-name {
    position: absolute;
    left: 270px;
    top: 128px;
    margin: 0;
    font-family: "Orbitron", sans-serif;
    font-weight: 700;
    color: var(--brand-lime);
    line-height: 1.1;
    letter-spacing: 1px;
  }
  .brand-name .brand-primary {
    display: block;
    font-size: 70px;
  }
  .brand-name .brand-secondary {
    display: block;
    font-size: 40px;
    letter-spacing: 3px;
  }
  .offer-panel {
    height: 456px;
    background: var(--sign-lime);
  }
  .offer-panel svg {
    display: block;
  }
  .service-main {
    font-family: "Orbitron", sans-serif;
    font-weight: 900;
    fill: var(--ink-black);
  }
  .service-sub {
    font-family: "Orbitron", sans-serif;
    font-weight: 700;
    fill: var(--ink-white);
  }
  .call-label {
    font-family: "Exo 2", sans-serif;
    font-weight: 700;
    fill: var(--ink-black);
  }
  .phone-number {
    font-family: "Orbitron", sans-serif;
    font-weight: 900;
    fill: var(--ink-black);
  }
  .rule {
    stroke: var(--ink-white);
    stroke-width: 4;
  }
</style>
</head>
<body>
  <main class="yard-sign">
    <header class="brand-panel">
      <span class="brand-mark" aria-hidden="true"></span>
      <h1 class="brand-name">
        <span class="brand-primary">BRANTLEY</span>
        <span class="brand-secondary">GROUNDS LLC</span>
      </h1>
    </header>
    <section class="offer-panel">
      <svg width="878" height="456" viewBox="0 0 878 456" xmlns="http://www.w3.org/2000/svg">
        <text class="service-main" x="439" y="149" text-anchor="middle" font-size="132" textLength="790" lengthAdjust="spacingAndGlyphs">MOWING</text>
        <line class="rule" x1="0" y1="225" x2="118" y2="225"/>
        <line class="rule" x1="760" y1="225" x2="878" y2="225"/>
        <text class="service-sub" x="439" y="248" text-anchor="middle" font-size="62" textLength="594" lengthAdjust="spacingAndGlyphs">LANDSCAPING</text>
        <text class="call-label" x="439" y="328" text-anchor="middle" font-size="50" textLength="397" lengthAdjust="spacingAndGlyphs">Call or Text</text>
        <text class="phone-number" x="439" y="420" text-anchor="middle" font-size="92" textLength="782" lengthAdjust="spacingAndGlyphs">555-204-7719</text>
      </svg>
    </section>
  </main>
</body>
</html>
```